Business Card Design

We are a new residential construction company.our team is made up of young highly skilled tradesman of the next generation of carpenters coming through with new skills and ideas.we chose the name meridian as it means strikingly different from the rest as this is what we plan to be and we would like to portray this in our business card.we like Bold lettering as we want to make a statement, also the use of colour would be great as we want to stand out from the usual plain construction cards and logos.
I have attached a logo sketch I did as a rough idea if you can tidy it up or improve on it would be good.
I have also attached the LBP logo please include this on the card small but still legible.
open to any colourschemes ideas.
thanks
(note)please delete the LBP#308617 off from the card details please.
Updates
Industry/Entity Type
Construction
Contact Information for Business Card
MERIDIAN CONSTRUCTION LIMITED
Director:Kai Pereira
Mobile :0217364801
Email:Meridian.Construction@examplemail.test
Address:48 Halvorsen place,Ashgrove park 2071,Auckland
LBP#BP308617
Look and feel
Each slider illustrates characteristics of the customer's brand and the style your logo design should communicate.

```html
<!DOCTYPE html>
<html lang="en">
<head>
<meta charset="utf-8">
<title>Meridian Construction Limited – Business Card</title>
<link rel="stylesheet" href="https://fonts.googleapis.com/css2?family=Cinzel:wght@700;900&family=Open+Sans:wght@700&display=swap">
<style>
  :root {
    --night: #060707;
    --mist: #dcdfe0;
    --ink: #1c1410;
    --glow: #f0892a;
    --echo: rgba(255, 255, 255, 0.85);
    --sky: #5cb9ee;
    --badge: #3d6fb6;
  }
  html, body {
    margin: 0;
    padding: 0;
    overflow: hidden;
    background: var(--mist);
  }
  .card {
    position: relative;
    width: 1200px;
    height: 741px;
    overflow: hidden;
    background: var(--mist);
  }
  .brand-band {
    position: absolute;
    left: 0;
    top: 0;
    width: 1200px;
    height: 414px;
    background: var(--night);
  }
  .brand-name {
    position: absolute;
    left: 0;
    right: 0;
    top: 128px;
    margin: 0;
    text-align: center;
    font-family: "Open Sans", sans-serif;
    font-weight: 700;
    font-size: 124px;
    line-height: 124px;
    letter-spacing: 3px;
    color: var(--sky);
  }
  .details {
    position: absolute;
    right: 27px;
    top: 446px;
    text-align: right;
    color: var(--ink);
    white-space: nowrap;
  }
  .details p {
    margin: 0;
    text-shadow:
      0 0 2px var(--glow),
      0 0 4px var(--glow),
      -16px -14px 5px var(--echo);
  }
  .company {
    font-family: "Cinzel", serif;
    font-weight: 900;
    font-size: 50px;
    line-height: 60px;
    letter-spacing: 0.5px;
  }
  .line {
    font-family: "Open Sans", sans-serif;
    font-weight: 700;
    font-size: 35px;
    line-height: 56px;
  }
  .lbp-badge {
    position: absolute;
    right: 27px;
    top: 676px;
    width: 52px;
    height: 52px;
    border-radius: 6px;
    background: var(--badge);
  }
</style>
</head>
<body>
<main class="card">
  <header class="brand-band">
    <h1 class="brand-name">MERIDIAN</h1>
  </header>
  <section class="details">
    <p class="company">MERIDIAN CONSTRUCTION LIMITED</p>
    <p class="line">Director: Kai Pereira&nbsp; Mobile: 0217364801</p>
    <p class="line">Email: Meridian.Construction@examplemail.test</p>
    <p class="line">Address: 48 Halvorsen place, Ashgrove park 2071 Auckland</p>
  </section>
  <div class="lbp-badge" role="img" aria-label="Licensed building practitioner badge"></div>
</main>
</body>
</html>
```